Book Cover Design Book About Commercial Real Estate Investing

I need a book cover designed for my upcoming book.
Need cover for paperback and hardcover book.

The Book is about investing in net lease commercial property.

The book title:

The Ground Rent Handbook
Proven Methods For KVR Asset Buyers
By Lou Barrow

Should be minimalist, clean, authoritative, convey money, trust, & growth
I think I like the colors white red and black.
I want a front cover at this time.

Samples I like are included. - the red white and blacks are my favorites

My company is The KVR Circle
you can learn more about Triple Net Properties at my website
www.TheKVRCircle.com

the symbol NNN = Triple net in commercial real estate

Target Market(s)

Affluent male conservative investors

Industry/Entity Type

Real Estate

Requirements
Nice to have
• Sports Motif - - diagrams of sports plays from playbook
• google - Diagrams of sports plays -

```html
<!DOCTYPE html>
<html lang="en">
<head>
<meta charset="utf-8">
<title>The Ground Rent Handbook — Lou Barrow</title>
<link rel="stylesheet" href="https://fonts.googleapis.com/css2?family=Bebas+Neue&family=Oswald:wght@500;600&display=swap">
<style>
  :root {
    --red: #c8161d;
    --red-dark: #8e0b10;
    --red-light: #e24a4f;
    --ink: #58585a;
    --ink-dark: #3a3a3c;
    --paper: #ffffff;
    --mist: #e9e9ea;
  }
  * { margin: 0; padding: 0; box-sizing: border-box; }
  html, body { width: 800px; height: 1200px; overflow: hidden; background: var(--paper); }
  .cover {
    position: relative;
    width: 800px;
    height: 1200px;
    background: var(--paper);
    overflow: hidden;
  }
  .band {
    position: absolute;
    left: 0;
    width: 800px;
    background: linear-gradient(90deg, var(--red-dark) 0%, var(--red-light) 50%, var(--red-dark) 100%);
  }
  .band--top { top: 0; height: 88px; display: flex; align-items: center; justify-content: center; }
  .band--bottom { bottom: 0; height: 22px; }
  .author {
    font-family: "Oswald", sans-serif;
    font-weight: 500;
    font-size: 58px;
    letter-spacing: 17px;
    color: var(--paper);
    padding-left: 17px;
    line-height: 1;
  }
  .title {
    position: absolute;
    top: 100px;
    left: 0;
    width: 800px;
    text-align: center;
    font-family: "Bebas Neue", sans-serif;
    color: var(--ink);
    line-height: 0.9;
  }
  .title__line--top { display: block; font-size: 142px; letter-spacing: 1px; }
  .title__line--main { display: block; font-size: 190px; letter-spacing: 3px; margin-top: 2px; }
  .subtitle {
    position: absolute;
    top: 408px;
    left: 0;
    width: 800px;
    text-align: center;
    font-family: "Oswald", sans-serif;
    font-weight: 600;
    font-size: 46px;
    line-height: 1.2;
    color: var(--red);
    text-transform: uppercase;
    letter-spacing: 0.5px;
  }
  .artwork {
    position: absolute;
    top: 540px;
    left: 95px;
    width: 610px;
    height: 560px;
    background:
      radial-gradient(ellipse 42% 40% at 52% 50%, var(--red) 0%, var(--red) 55%, rgba(200,22,29,0) 100%),
      radial-gradient(ellipse 60% 60% at 50% 50%, var(--mist) 0%, var(--paper) 100%);
  }
  .publisher {
    position: absolute;
    top: 1118px;
    left: 0;
    width: 800px;
    display: flex;
    align-items: center;
    justify-content: center;
    gap: 12px;
  }
  .publisher__mark {
    width: 34px;
    height: 34px;
    background: var(--ink-dark);
  }
  .publisher__name {
    font-family: "Oswald", sans-serif;
    font-weight: 600;
    font-size: 32px;
    color: var(--red);
    text-transform: uppercase;
    line-height: 1;
  }
</style>
</head>
<body>
  <main class="cover">
    <header class="band band--top">
      <p class="author">LOU BARROW</p>
    </header>

    <h1 class="title">
      <span class="title__line--top">THE GROUND RENT</span>
      <span class="title__line--main">HANDBOOK</span>
    </h1>

    <p class="subtitle">Proven Methods<br>For KVR Asset Buyers</p>

    <div class="artwork" role="img" aria-label="Illustration of red jigsaw puzzle pieces forming a white house symbol, over a field of scattered white puzzle pieces"></div>

    <footer class="publisher">
      <span class="publisher__mark"></span>
      <span class="publisher__name">The KVR Circle</span>
    </footer>

    <div class="band band--bottom"></div>
  </main>
</body>
</html>
```